Creative Redesign for VEK Polymer 2024 Product Brochure

"VEK Polymer is seeking a creative and experienced graphic designer to create a new design layout for our 2024 brochure. Our objective is to transform our current brochure into a more modern and visually appealing document that aligns with our evolving brand identity. The brochure should not only reflect our company's ethos of innovation and quality but also effectively showcase our range of plastic solutions and services. We aim to achieve a design that is both informative and engaging, capable of capturing the attention of our diverse clientele in the industrial sector."
Target Market(s)
Details: "Our primary audience includes professionals in the manufacturing, automotive, and healthcare industries who value quality and innovative plastic solutions."
Industry/Entity Type
Plastics Manufacturing
Font styles to use
- Preferences: Primary Font: Sans Serif (for clear readability across digital and print formats) Secondary Font: Serif (for titles and headings to add contrast)
Colors
Designer to choose colors to be used in the design.
Requirements
Must have
- "Inclusion of our company logo and color scheme" "Sections for each major service and product line"
Should not have
- "Overly complex jargon that may confuse non-specialist readers" "Cluttered visual elements that detract from the content's readability"

```html
<!DOCTYPE html>
<html lang="da">
<head>
<meta charset="utf-8">
<title>VEK Polymer – Brochure 2024</title>
<link href="https://fonts.googleapis.com/css2?family=Montserrat:wght@300;400;600;700&family=Open+Sans:wght@400;600&family=Tinos:wght@400;700&display=swap" rel="stylesheet">
<style>
:root{
  --red:#c1272d;
  --red-dk:#8e1a1f;
  --ink:#231f20;
  --backdrop:#a8aaa9;
  --paper:#ffffff;
  --text:#3b3b3b;
  --rule:#9a9a9a;
  --wedge-grey:#d9d9d9;
}
*{box-sizing:border-box}
html,body{margin:0;padding:0}
body{width:1200px;height:1143px;overflow:hidden;background:var(--backdrop);position:relative;font-family:"Tinos",serif}
.spread{position:absolute;width:352px;height:251px;display:flex;box-shadow:0 1px 3px rgba(0,0,0,.25)}
.page{flex:1;position:relative;background:var(--paper);overflow:hidden}
.page+.page{box-shadow:inset 3px 0 4px -3px rgba(0,0,0,.18)}
.tr{position:absolute;top:0;right:0;width:82px;height:30px;background:linear-gradient(200deg,#ececec,#cfcfcf);clip-path:polygon(0 0,100% 0,100% 100%)}
.tr::after{content:"";position:absolute;inset:0;background:linear-gradient(90deg,var(--red-dk),var(--red));clip-path:polygon(48% 0,100% 0,100% 72%)}
.bl{position:absolute;bottom:0;left:0;width:42px;height:36px;background:var(--wedge-grey);clip-path:polygon(0 0,100% 100%,0 100%)}
.bl::after{content:"";position:absolute;inset:0;background:linear-gradient(0deg,var(--red-dk),var(--red));clip-path:polygon(0 38%,78% 100%,0 100%)}
.hd{position:absolute;top:8px;left:10px;display:flex;align-items:flex-end;gap:5px}
.brand{display:flex;flex-direction:column;align-items:center;padding-right:5px;border-right:.4px solid var(--rule)}
.brand b{font:700 5.6px/1 "Tinos",serif;color:var(--ink)}
.brand span{font:400 2.5px/1.4 "Montserrat",sans-serif;color:var(--ink)}
.motto{font:400 3.8px/1 "Montserrat",sans-serif;color:#333}
.title{position:absolute;left:10px;top:27px;right:10px;margin:0;font:400 7px/1.12 "Montserrat",sans-serif;color:var(--red)}
.title strong{font-weight:700;display:block}
.block{position:absolute}
.lead{margin:0 0 2px;font:700 2.3px/1.42 "Tinos",serif;color:var(--red)}
.lead.soft{font-weight:400}
.tx{margin:0 0 1.4px;font:400 2.3px/1.42 "Tinos",serif;color:var(--text)}
.h{margin:1.6px 0 .8px;font:400 3.9px/1.1 "Montserrat",sans-serif;color:var(--red)}
.ph{position:absolute}
.ft{position:absolute;bottom:6px;left:24px;right:10px;display:flex;gap:7px;align-items:center;font:400 2.8px/1 "Montserrat",sans-serif;color:#333}
.ft .pn{margin-left:auto}
.ft.left .pn{margin-left:0;color:#fff;position:absolute;left:-14px}
.ic{width:3.4px;height:3.4px;vertical-align:-.6px;margin-right:1px;fill:var(--red)}
.bullets{margin:0 0 1.5px;padding-left:5px;font:400 2.3px/1.42 "Tinos",serif;color:var(--text)}
.bullets li::marker{color:var(--red)}
.bullets b{color:var(--red)}
.cover-band{position:absolute;left:0;right:0;top:64px;height:123px;background:var(--ink)}
.cover-logo{position:absolute;left:0;right:0;text-align:center;font:700 9px/1 "Tinos",serif;color:var(--ink)}
.cover-sub{position:absolute;left:0;right:0;text-align:center;font:400 3.2px "Montserrat",sans-serif;color:var(--red)}
.cover-claim{position:absolute;left:0;right:0;text-align:center;font:700 6.2px "Tinos",serif;color:var(--red)}
.cover-big{position:absolute;left:0;right:0;top:190px;text-align:center;font:300 12.5px/1.15 "Montserrat",sans-serif;color:var(--red);margin:0}
.contact{position:absolute;top:194px;left:18px;right:18px;display:flex;font:400 3px/1.6 "Tinos",serif;color:var(--ink)}
.contact>div{flex:1;text-align:center}
.contact>div+div{border-left:.4px solid var(--rule)}
.contact b{font-size:4.6px}
.statement{display:flex;align-items:center;justify-content:center;text-align:center;padding:0 22px;font:400 4.4px/1.95 "Open Sans",sans-serif;color:#fff}
.statement p{margin:0 0 8px}
.bg-red{background:var(--red-dk)}
.bg-ink{background:var(--ink)}
.toc{position:absolute;top:62px;left:10px;right:12px;margin:0;padding:0;list-style:none;font:400 2.4px/1 "Tinos",serif;color:var(--text)}
.toc li{display:flex;gap:2px;margin-bottom:4.2px}
.toc li::after{content:"";order:1;flex:1;border-bottom:.3px dotted #777}
.toc li span{order:2}
.tbl{border-collapse:collapse;width:100%;font:400 2.1px/1.3 "Tinos",serif;color:var(--text)}
.tbl th{background:var(--red);color:#fff;font-weight:700;text-align:left;padding:.8px 1.5px}
.tbl td{padding:.9px 1.5px;border-bottom:.3px solid #ddd;vertical-align:top}
.tbl tr:nth-child(even) td{background:#f6eeee}
.badge{position:absolute;border-radius:50%}
.seal{position:absolute;border-radius:2px}
.help-band{position:absolute;left:0;right:0;top:56px;height:143px;background:var(--red-dk);color:#fff;text-align:center;padding:26px 18px 0}
.help-band h2{margin:0 0 10px;font:600 6.3px "Montserrat",sans-serif}
.help-band p{margin:0 0 4px;font:400 2.4px/1.55 "Tinos",serif}
</style>
</head>
<body>
<svg width="0" height="0" style="position:absolute" aria-hidden="true">
  <symbol id="i-phone" viewBox="0 0 24 24"><path d="M6.6 10.8a15 15 0 0 0 6.6 6.6l2.2-2.2a1 1 0 0 1 1-.25 11.4 11.4 0 0 0 3.6.6 1 1 0 0 1 1 1V20a1 1 0 0 1-1 1A17 17 0 0 1 3 4a1 1 0 0 1 1-1h3.5a1 1 0 0 1 1 1c0 1.25.2 2.45.6 3.6a1 1 0 0 1-.25 1z"/></symbol>
  <symbol id="i-globe" viewBox="0 0 24 24"><path d="M12 2a10 10 0 1 0 0 20 10 10 0 0 0 0-20zm0 2c.9 1.2 1.6 2.7 2 4h-4c.4-1.3 1.1-2.8 2-4zM4.3 14a8 8 0 0 1 0-4h3.4a16 16 0 0 0 0 4zm.8 2h3c.3 1.3.8 2.5 1.4 3.6A8 8 0 0 1 5.1 16zm3-8h-3a8 8 0 0 1 4.4-3.6C7.9 5.5 7.4 6.7 8.1 8zM12 20c-.9-1.2-1.6-2.7-2-4h4c-.4 1.3-1.1 2.8-2 4zm2.3-6H9.7a14 14 0 0 1 0-4h4.6a14 14 0 0 1 0 4zm.3 5.6c.6-1.1 1.1-2.3 1.4-3.6h3a8 8 0 0 1-4.4 3.6zM16.3 14a16 16 0 0 0 0-4h3.4a8 8 0 0 1 0 4z"/></symbol>
  <symbol id="i-pin" viewBox="0 0 24 24"><path d="M12 2a7 7 0 0 0-7 7c0 5 7 13 7 13s7-8 7-13a7 7 0 0 0-7-7zm0 9.5A2.5 2.5 0 1 1 12 6.5a2.5 2.5 0 0 1 0 5z"/></symbol>
  <symbol id="i-mail" viewBox="0 0 24 24"><path d="M3 5h18v14H3zm2 2v.5l7 4.5 7-4.5V7zm0 2.8V17h14V9.8l-7 4.5z"/></symbol>
</svg>

<!-- Row 1 -->
<section class="spread" style="left:56px;top:43px">
  <article class="page">
    <i class="tr"></i><i class="bl"></i>
    <div class="cover-logo" style="top:19px;font-size:7px">VEK Polymer</div>
    <div class="cover-sub" style="top:29px">Din partner i plastforarbejdning</div>
    <div class="cover-claim" style="top:44px">Vi gør din vision til virkelighed</div>
    <div class="cover-band"></div>
    <div class="ph" style="left:8px;right:8px;top:72px;height:108px;background:radial-gradient(circle at 72% 22%,#c0303a 0 4%,transparent 9%),radial-gradient(ellipse at 40% 85%,#5a4a7a 0 18%,transparent 40%),linear-gradient(180deg,#2a2434,#4a3a3a 55%,#2a1c1a)" role="img" aria-label="Koncertsal med kor på scenen og en rød stjernelampe"></div>
    <div class="contact">
      <div><svg class="ic"><use href="#i-pin"/></svg><br><b>VEK Polymer A/S</b><br>Industrivej 12, Hørning<br>DK-8362 Hørning<br>CVR-nr 12345678</div>
      <div><svg class="ic"><use href="#i-phone"/></svg><br>40 12 34 56<br><svg class="ic"><use href="#i-mail"/></svg><br>info@vekpolymer.dk<br><svg class="ic"><use href="#i-globe"/></svg><br>www.vekpolymer.dk</div>
    </div>
  </article>
  <article class="page">
    <i class="tr"></i><i class="bl"></i>
    <div class="cover-logo" style="top:24px;font-size:11px">VEK Polymer</div>
    <div class="cover-sub" style="top:44px">Din partner i plastforarbejdning</div>
    <div class="cover-band"></div>
    <div class="ph" style="left:2px;width:85px;top:70px;height:55px;background:linear-gradient(135deg,#f2f2f2,#b9b9b9 60%,#6a6a6a)" role="img" aria-label="Hvide bearbejdede plastemner"></div>
    <div class="ph" style="left:89px;width:85px;top:70px;height:55px;background:linear-gradient(135deg,#b0b3b8,#5b5e63 50%,#e8e8e8)" role="img" aria-label="CNC-drejebænk i arbejde"></div>
    <div class="ph" style="left:2px;width:85px;top:127px;height:56px;background:linear-gradient(135deg,#30343a,#767a80 50%,#25272a)" role="img" aria-label="CNC-fræser med plastemne"></div>
    <div class="ph" style="left:89px;width:85px;top:127px;height:56px;background:linear-gradient(135deg,#e9e4d8,#a89a7a 55%,#3a3632)" role="img" aria-label="Plastdele og betalingsterminal-holder"></div>
    <h1 class="cover-big">Vi gør din vision<br>til virkelighed</h1>
    <footer class="ft" style="left:54px"><span><svg class="ic"><use href="#i-phone"/></svg>40 12 34 56</span><span><svg class="ic"><use href="#i-globe"/></svg>www.vekpolymer.dk</span></footer>
  </article>
</section>

<section class="spread" style="left:422px;top:43px;width:356px">
  <article class="page bg-red statement">
    <div><p>VEK Polymer A / S<br>offers high quality tailor-made<br>plastic solutions. With advanced<br>technology and a dedicated team of<br>plastic specialists and engineers, we<br>design solutions for every need.</p>
    <p>Our uncompromising approach to<br>quality ensures first-class finish and<br>durability – essential to both yours<br>and our success.</p></div>
  </article>
  <article class="page bg-ink statement">
    <div><p>Since 1986 we at VEK Polymer have<br>offered total solutions in plastic.</p>
    <p>With over 35 years of experience in<br>plastic machining we can help with<br>everything from idea development to<br>finished products.</p>
    <p>Need inspiration for your next project,<br>we are happy to contribute ideas for<br>material selection and innovative<br>solutions.</p></div>
  </article>
</section>

<section class="spread" style="left:791px;top:43px">
  <article class="page">
    <i class="tr"></i><i class="bl"></i>
    <header class="hd"><div class="brand"><b>VEK Polymer</b><span>Din partner i plastforarbejdning</span></div><span class="motto">Vi gør din vision til virkelighed</span></header>
    <h2 class="title" style="top:34px">Inhaltsübersicht</h2>
    <ol class="toc">
      <li>VEK Polymer A/S<span>1</span></li>
      <li>Avanceret softwareintegration hos VEK Polymer<span>2</span></li>
      <li>CNC-fræsning og robotautomatisering<span>3</span></li>
      <li>CNC Drejning af Tekniske Plastemner<span>4</span></li>
      <li>Vakuumformning: Fra Koncept til Færdigt Produkt<span>5</span></li>
      <li>Plastsvejsning: Nøglen til Robuste Plastkomponenter<span>6</span></li>
      <li>Limning af plastmaterialer<span>7</span></li>
      <li>Bukning af plastmaterialer<span>8</span></li>
      <li>Polering af Plast: Forfining af Overflader til Perfektion<span>9</span></li>
      <li>Laserskæring af Plast<span>10</span></li>
      <li>Bæredygtighed og Stabilitet hos VEK Polymer<span>11</span></li>
      <li>Plastløsninger til Fødevareindustrien<span>12</span></li>
      <li>Maskinafskærmning og Innovativt Maskindesign<span>13</span></li>
      <li>Tilpassede Nyseskærme og Udstillingsmontrer<span>14</span></li>
      <li>Oversigt over Tekniske Plastmaterialer<span>15-16</span></li>
      <li>VEK Polymer: Din Partner i Skræddersyede Plastløsninger<span>17</span></li>
      <li>Vi står klar til at hjælpe dig<span>18-19</span></li>
    </ol>
    <footer class="ft left"><span class="pn">IV</span><span><svg class="ic"><use href="#i-phone"/></svg>40 12 34 56</span><span><svg class="ic"><use href="#i-globe"/></svg>www.vekpolymer.dk</span></footer>
  </article>
  <article class="page">
    <i class="tr"></i><i class="bl"></i>
    <header class="hd"><div class="brand"><b>VEK Polymer</b><span>Din partner i plastforarbejdning</span></div><span class="motto">Vi gør din vision til virkelighed</span></header>
    <h2 class="title">VEK Polymer A/S</h2>
    <div class="block" style="top:42px;left:10px;width:74px">
      <p class="tx">Velkommen til VEK Polymer, en virksomhed, hvor avanceret teknologi og mere end 35 års erfaring kombineres for at levere skræddersyede, innovative plastløsninger til et bredt spektrum af industrier. Med dybtgående knowhow og et alsidigt maskinpark, herunder avanceret CNC-fræsning og drejning, laserskæring, plastsvejsning, vakuumformning, samt limning og varmebukning af plast, tilbyder vi alt fra enkelte prototyper til store serier. Vores medarbejdere har mange års erfaring med tekniske plastmaterialer, og vi rådgiver gerne om både design, materialevalg og den mest økonomiske produktionsmetode til netop din opgave.</p>
    </div>
    <div class="block" style="top:42px;left:90px;width:76px">
      <p class="tx">Hos VEK Polymer stræber vi ikke blot efter at opfylde, men også at overgå vores kunders forventninger ved at tilbyde komplette løsninger fra idé til det færdige produkt. Vores team af ingeniører arbejder tæt sammen med dig omkring materialevalg og design for at sikre, at dit projekt bliver en succes. Vi lægger vægt på kvalitet, korte leveringstider og en personlig service, der gør samarbejdet enkelt og trygt for alle parter.</p>
    </div>
    <div class="ph" style="left:10px;width:58px;top:103px;height:88px;background:linear-gradient(160deg,#fafafa,#dcdcdc 50%,#2a2a2c 80%)" role="img" aria-label="Hvid plastholder til betalingsterminal"></div>
    <div class="ph" style="left:72px;width:94px;top:103px;height:88px;background:radial-gradient(ellipse at 55% 45%,#e8e8e8 0 22%,#8a8a8a 40%,#1f1f21 70%)" role="img" aria-label="Hvide fræsede plastkomponenter på sort baggrund"></div>
    <p class="lead soft" style="position:absolute;top:195px;left:10px;width:80px;font-size:2.8px">"Vi tilbyder fremragende service til konkurrencedygtige priser og med hurtige leveringstider.</p>
    <footer class="ft" style="left:80px"><span><svg class="ic"><use href="#i-phone"/></svg>40 12 34 56</span><span><svg class="ic"><use href="#i-globe"/></svg>www.vekpolymer.dk</span><span class="pn">1</span></footer>
  </article>
</section>

<!-- Row 2 -->
<section class="spread" style="left:56px;top:306px">
  <article class="page">
    <i class="tr"></i><i class="bl"></i>
    <header class="hd"><div class="brand"><b>VEK Polymer</b><span>Din partner i plastforarbejdning</span></div><span class="motto">Vi gør din vision til virkelighed</span></header>
    <h2 class="title">Avanceret softwareintegration<br>hos VEK Polymer</h2>
    <p class="lead block" style="top:46px;left:10px;right:10px">Hos VEK Polymer benytter vi branchens førende software for at sikre præcision og effektivitet i vores produktionsprocesser. Vi anvender PathCAM, ContourCAM og ModelForm, som hver især spiller en afgørende rolle i designet.</p>
    <div class="ph" style="left:10px;width:105px;top:62px;height:74px;background:radial-gradient(ellipse at 30% 40%,#c9a86a 0 10%,transparent 30%),linear-gradient(135deg,#4a4d52,#1a1b1e 60%,#5b5e62)" role="img" aria-label="Fræseværktøjer i maskinmagasin"></div>
    <div class="ph" style="left:86px;width:76px;top:120px;height:44px;background:linear-gradient(135deg,#f3f3f3,#c8d3dc 45%,#7aa05a 70%,#e2e2e2);box-shadow:0 0 2px rgba(0,0,0,.3)" role="img" aria-label="Skærmbillede af CAD-modellering"></div>
    <div class="block" style="top:148px;left:10px;width:70px">
      <h3 class="h">PathCAM</h3>
      <p class="tx">er et førende CAM-værktøj, optimeret til bearbejdning af plastkomponenter. Det giver os mulighed for at programmere komplekse CNC-maskiner til at producere emner med stor nøjagtighed. PathCAM styrer både 3- og 5-akse bearbejdning og sikrer en ensartet kvalitet fra første til sidste emne i produktionen.</p>
      <h3 class="h">ContourCAM</h3>
      <p class="tx">er et værktøj til vores værktøjsbaner, som understøtter fremstilling af komplekse dele gennem avancerede bearbejdningsstrategier. Dette sikrer optimal bearbejdning ved at minimere maskintid og materialespild, samtidig med at vi opnår glatte overflader og høj gentagelsesnøjagtighed.</p>
    </div>
    <div class="block" style="top:168px;left:86px;width:76px">
      <h3 class="h">ModelForm</h3>
      <p class="tx">anvendes i designfasen, hvor vores ingeniører designer nøjagtige 3D-modeller af de ønskede komponenter. Dette værktøj giver en detaljeret modellering af former og geometrier. Ved at anvende dette program kan vi hurtigt justere designs efter kundens behov, lave tegninger til godkendelse og sikre perfekt pasform i produktionen. Modellerne overføres direkte til vores CAM-systemer, hvilket eliminerer fejl og forkorter tiden fra idé til færdigt emne betydeligt.</p>
    </div>
    <footer class="ft left"><span class="pn">2</span><span><svg class="ic"><use href="#i-phone"/></svg>40 12 34 56</span><span><svg class="ic"><use href="#i-globe"/></svg>www.vekpolymer.dk</span></footer>
  </article>
  <article class="page">
    <i class="tr"></i><i class="bl"></i>
    <header class="hd"><div class="brand"><b>VEK Polymer</b><span>Din partner i plastforarbejdning</span></div><span class="motto">Vi gør din vision til virkelighed</span></header>
    <h2 class="title">CNC-fræsning og robotautomatisering</h2>
    <p class="lead block" style="top:37px;left:10px;right:10px">Hos VEK Polymer er vi førende inden for CNC-fræsning af tekniske plastemner. Præcision og pålidelighed er nøgleordene, når vi fremstiller komplekse komponenter. Vores produktionsfaciliteter er udstyret med avancerede maskiner, herunder 5-akse fræsere og robotcelle.</p>
    <div class="ph" style="left:15px;width:153px;top:56px;height:86px;background:radial-gradient(ellipse at 80% 35%,#e2b21e 0 12%,transparent 30%),linear-gradient(135deg,#7c7f84,#3a3c40 55%,#9a9ca0)" role="img" aria-label="Fræsemaskine med gul robotarm"></div>
    <div class="block" style="top:150px;left:15px;width:74px">
      <p class="tx">For at optimere vores produktion er vi udstyret med robotteknologi, der muliggør effektiv drift døgnet rundt. Robotterne håndterer emner med høj præcision og konsistens, hvilket reducerer ledetider og sikrer ensartet kvalitet i alle serier.</p>
      <p class="tx">Vores 5-akse CNC-maskiner muliggør simultan bearbejdning, hvilket betyder at komplekse geometrier kan fræses i én opspænding. Dette giver bedre præcision og kortere produktionstider for vores kunder.</p>
      <p class="tx">Dedikeret til teknisk præcision sikrer vores konstant opdaterede maskinpark, at alle dele fremstilles efter de højeste industrielle standarder og leveres til tiden.</p>
    </div>
    <div class="ph" style="left:94px;width:74px;top:150px;height:52px;background:linear-gradient(135deg,#2b2d31,#6b6e73 45%,#1c1d20)" role="img" aria-label="Maskinrum med CNC-fræsere"></div>
    <div class="block" style="top:205px;left:94px;width:74px">
      <p class="tx">CNC-fræsning muliggør produktion af højpræcisionsdele til en bred vifte af industrier, herunder medicinsk udstyr, fødevareindustri og elektronik. Kontakt os for at høre mere.</p>
    </div>
    <footer class="ft" style="left:80px"><span><svg class="ic"><use href="#i-phone"/></svg>40 12 34 56</span><span><svg class="ic"><use href="#i-globe"/></svg>www.vekpolymer.dk</span><span class="pn">3</span></footer>
  </article>
</section>

<section class="spread" style="left:422px;top:306px;width:356px">
  <article class="page">
    <i class="tr"></i><i class="bl"></i>
    <header class="hd"><div class="brand"><b>VEK Polymer</b><span>Din partner i plastforarbejdning</span></div><span class="motto">Vi gør din vision til virkelighed</span></header>
    <h2 class="title">CNC Drejning af Tekniske Plastemner</h2>
    <p class="lead block" style="top:37px;left:11px;right:10px">Hos VEK Polymer tilbyder vi CNC-drejning af tekniske plastemner, hvor avanceret udstyr og stor erfaring sikrer høj præcision og effektivitet. Vores drejeafdeling leverer komponenter til mange industrier, fra enkelte emner til store serier.</p>
    <div class="ph" style="left:11px;width:136px;top:57px;height:66px;background:radial-gradient(ellipse at 55% 60%,#e8e8e8 0 10%,transparent 25%),linear-gradient(135deg,#55585d,#1f2023 50%,#6e7176)" role="img" aria-label="CNC-drejebænk med plastemne"></div>
    <div class="ph" style="left:11px;width:65px;top:145px;height:49px;background:linear-gradient(135deg,#5a1a1d,#f1ece6 30%,#d9d2c9 70%,#8a8a8a)" role="img" aria-label="Hvide drejede plastdele"></div>
    <div class="block" style="top:198px;left:11px;width:68px">
      <h3 class="h">Teknik og Udstyr</h3>
      <p class="tx">Vores CNC-drejebænke er optimeret til plastbearbejdning, hvilket gør det muligt at producere dele med snævre tolerancer og fine overflader. Vi drejer emner i diametre fra få millimeter til store ringe og bøsninger.</p>
    </div>
    <div class="block" style="top:144px;left:82px;width:85px">
      <h3 class="h">Materialehåndtering og Bearbejdning</h3>
      <p class="tx">Vi arbejder med en lang række materialer, herunder POM, PEHD, PA og PTFE, og kender deres egenskaber under bearbejdning, så vi kan vælge de rette værktøjer og skærehastigheder.</p>
      <h3 class="h">Ekspertise og Kvalitetssikring</h3>
      <p class="tx">Vores team af erfarne teknikere sikrer, at alle emner kontrolleres løbende mod tegning og specifikationer, så kvaliteten er i orden hver gang.</p>
      <h3 class="h">Hurtig og Effektiv Produktion</h3>
      <p class="tx">Vi effektiviserer vores produktionsprocesser for at sikre hurtige leveringstider, uden at gå på kompromis med kvaliteten. Vores automatiserede stangfødning gør det muligt at producere større serier økonomisk.</p>
    </div>
    <footer class="ft left"><span class="pn">4</span><span><svg class="ic"><use href="#i-phone"/></svg>40 12 34 56</span><span><svg class="ic"><use href="#i-globe"/></svg>www.vekpolymer.dk</span></footer>
  </article>
  <article class="page">
    <i class="tr"></i><i class="bl"></i>
    <header class="hd"><div class="brand"><b>VEK Polymer</b><span>Din partner i plastforarbejdning</span></div><span class="motto">Vi gør din vision til virkelighed</span></header>
    <h2 class="title"><strong>Vakuumformning:</strong>Fra Koncept til Færdigt Produkt</h2>
    <div class="ph" style="left:15px;width:146px;top:47px;height:74px;background:radial-gradient(ellipse at 55% 48%,#a6d63e 0 30%,#7fae2a 38%,#fff 52%)" role="img" aria-label="Grøn vakuumformet robotkabine på hjul"></div>
    <div class="ph" style="left:15px;width:73px;top:124px;height:51px;background:linear-gradient(160deg,#e9e9e9,#3a3b3e 35%,#1b1c1e 70%,#cfcfcf)" role="img" aria-label="Sort vakuumformet bakke"></div>
    <div class="block" style="top:178px;left:15px;width:74px">
      <p class="lead">Hos VEK Polymer er vi anerkendte eksperter inden for vakuumformning. Med vores omfattende erfaring leverer vi løsninger fra prototype til serie, tilpasset netop dine krav til form og funktion.</p>
      <ul class="bullets"><li><b>ABS:</b> Robust og slagfast, ideelt til kabinetter og afdækninger.</li><li><b>PS:</b> Let og økonomisk til emballage.</li><li><b>PETG:</b> Klar og fødevaregodkendt.</li></ul>
    </div>
    <div class="block" style="top:128px;left:95px;width:72px">
      <ul class="bullets"><li><b>PC:</b> Kendt for sin styrke og klarhed, ideel til krævende applikationer.</li><li><b>PVC:</b> Alsidig og kemikaliebestandig til mange formål.</li><li><b>PMMA (Akryl):</b> Værdsat for høj glans og optisk klarhed.</li><li><b>PEHD:</b> Høj kemisk modstand og slidstyrke.</li><li><b>PP:</b> Let og fleksibel med god kemisk modstand.</li></ul>
      <p class="tx">Vores teknologi sikrer, at hver formning er præcis og gentagelig, hvilket gør os til en pålidelig partner for både små og store virksomheder.</p>
      <p class="tx">For at diskutere dit næste projekt er du velkommen til at kontakte os. Vi hjælper med alt fra værktøj til færdigt emne.</p>
    </div>
    <footer class="ft" style="left:80px"><span><svg class="ic"><use href="#i-phone"/></svg>40 12 34 56</span><span><svg class="ic"><use href="#i-globe"/></svg>www.vekpolymer.dk</span><span class="pn">5</span></footer>
  </article>
</section>

<section class="spread" style="left:791px;top:306px">
  <article class="page">
    <i class="tr"></i><i class="bl"></i>
    <header class="hd"><div class="brand"><b>VEK Polymer</b><span>Din partner i plastforarbejdning</span></div><span class="motto">Vi gør din vision til virkelighed</span></header>
    <h2 class="title"><strong>Plastsvejsning:</strong>Nøglen til Robuste Plastkomponenter</h2>
    <p class="lead block" style="top:44px;left:10px;right:10px">Plastsvejsning er en fundamental teknik hos VEK Polymer, der muliggør sammensætningen af plastmaterialer til stærke og holdbare konstruktioner. Vi anvender en række metoder, tilpasset de specifikke krav til hver opgave.</p>
    <div class="ph" style="left:10px;width:156px;top:60px;height:76px;background:linear-gradient(180deg,#cfd2d4,#f0efea 35%,#5a5c60 60%,#2a2b2e)" role="img" aria-label="Lang svejset plastkonstruktion i værksted"></div>
    <div class="ph" style="left:10px;width:80px;top:138px;height:39px;background:linear-gradient(135deg,#2a2b2e,#f2f2f2 40%,#dadada 70%,#2a2b2e)" role="img" aria-label="Hvide svejste plastprofiler"></div>
    <div class="ph" style="left:92px;width:74px;top:138px;height:39px;background:linear-gradient(135deg,#d8d8d8,#3a3b3e 45%,#1d1e20)" role="img" aria-label="Sort plastplade med huller"></div>
    <div class="block" style="top:180px;left:10px;width:74px">
      <h3 class="h">Varm luft svejsning</h3>
      <p class="tx">Anvendes ofte til reparationer og samlinger, hvor en præcis og kontrolleret varme er nødvendig. Metoden er fleksibel og velegnet til tynde plader og komplekse former.</p>
      <h3 class="h">Ekstruderingssvejsning</h3>
      <p class="tx">Ideel til større konstruktioner med tykke materialer som PEHD og PP, hvor der kræves stærke og tætte samlinger, eksempelvis tanke og kar.</p>
    </div>
    <div class="block" style="top:180px;left:92px;width:74px">
      <h3 class="h">Ultralydssvejsning</h3>
      <p class="tx">Anvender højfrekvente lydbølger til at generere varme ved sammenføjningen, hvilket giver hurtige og rene samlinger uden tilsætningsmateriale. Metoden er særligt velegnet til små præcisionsdele i store serier.</p>
      <p class="tx">Vi rådgiver altid om den bedste svejsemetode til dit projekt.</p>
    </div>
    <footer class="ft left"><span class="pn">6</span><span><svg class="ic"><use href="#i-phone"/></svg>40 12 34 56</span><span><svg class="ic"><use href="#i-globe"/></svg>www.vekpolymer.dk</span></footer>
  </article>
  <article class="page">
    <i class="tr"></i><i class="bl"></i>
    <header class="hd"><div class="brand"><b>VEK Polymer</b><span>Din partner i plastforarbejdning</span></div><span class="motto">Vi gør din vision til virkelighed</span></header>
    <h2 class="title">Limning af plastmaterialer</h2>
    <p class="lead block" style="top:37px;left:14px;right:10px">Hos VEK Polymer forstår vi vigtigheden af at vælge de rette klæbemidler og behandlingsmetoder for at sikre både funktionalitet og æstetik i de endelige produkter.</p>
    <div class="ph" style="left:14px;width:90px;top:55px;height:61px;background:linear-gradient(135deg,#f4f6f7,#d4dde2 55%,#b8a79a)" role="img" aria-label="Hånd der holder limet akrylkasse"></div>
    <div class="ph" style="left:107px;width:59px;top:55px;height:61px;background:radial-gradient(ellipse at 50% 70%,#c6a530 0 12%,transparent 28%),linear-gradient(180deg,#1d1e21,#3a3b40)" role="img" aria-label="Akrylmontre med gul pyramide"></div>
    <div class="block" style="top:122px;left:14px;width:74px">
      <h3 class="h">Limningsprocessen:</h3>
      <p class="tx">Vores limningsproces kræver høj præcision og en gennemtænkt forberedelse. Overfladerne rengøres og behandles for at sikre den bedst mulige vedhæftning og et pænt resultat.</p>
      <h3 class="h">UV-Limning:</h3>
      <p class="tx">En særlig teknik, vi ofte anvender, især for vores glasklare materialer som PMMA, er UV-limning. Denne metode giver usynlige samlinger med høj styrke.</p>
      <h3 class="h">Specialisering og Tilpasning:</h3>
      <p class="tx">Vi tilpasser hver limningsopgave til de specifikke krav fra kunden, uanset om det gælder montrer, skilte eller tekniske komponenter.</p>
    </div>
    <div class="block" style="top:122px;left:93px;width:73px">
      <h3 class="h">Udfordringer ved Limning af Plast:</h3>
      <p class="tx">Nogle tekniske plastmaterialer som POM, PA og PEHD har lav overfladeenergi, hvilket gør dem svære at lime. Her bruger vi særlige metoder og primere for at opnå stærke og holdbare forbindelser.</p>
      <p class="tx">Vores tilgang til limning er både innovativ og fleksibel, så vi altid finder den mest holdbare løsning til dit behov.</p>
    </div>
    <footer class="ft" style="left:80px"><span><svg class="ic"><use href="#i-phone"/></svg>40 12 34 56</span><span><svg class="ic"><use href="#i-globe"/></svg>www.vekpolymer.dk</span><span class="pn">7</span></footer>
  </article>
</section>

<!-- Row 3 -->
<section class="spread" style="left:56px;top:571px">
  <article class="page">
    <i class="tr"></i><i class="bl"></i>
    <header class="hd"><div class="brand"><b>VEK Polymer</b><span>Din partner i plastforarbejdning</span></div><span class="motto">Vi gør din vision til virkelighed</span></header>
    <h2 class="title">Bukning af plastmaterialer</h2>
    <p class="lead block" style="top:37px;left:10px;right:10px">Hos VEK Polymer benytter vi både kold- og varmebukningsteknikker for at opnå præcision og tilpasse plastmaterialer til specifikke formål. Vores faciliteter er udstyret til både enkeltemner og større serier.</p>
    <div class="ph" style="left:10px;width:112px;top:57px;height:67px;background:linear-gradient(135deg,#c9ced2,#4f7898 40%,#26445c 75%,#8a9299)" role="img" aria-label="Bukkemaskine med blå plastplade"></div>
    <div class="ph" style="left:125px;width:41px;top:57px;height:67px;background:linear-gradient(160deg,#f5f5f5,#e84a3a 45%,#1f2024 75%)" role="img" aria-label="Rød og sort bukket plastkasse"></div>
    <div class="block" style="top:132px;left:10px;width:74px">
      <h3 class="h">Akryl (PMMA):</h3><p class="tx">Fremragende til varmebukning på grund af sin lave blødgøringstemperatur og gode klarhed. Anvendes ofte til skilte og displays.</p>
      <h3 class="h">PC (Polycarbonat):</h3><p class="tx">Kendt for sin fremragende slagstyrke og holdbarhed. PC er velegnet til afskærmninger og beskyttelsesdele.</p>
      <h3 class="h">PETG:</h3><p class="tx">Kendetegnet ved fremragende kemikalieresistens og god bukkeevne, også ved kold bukning.</p>
      <h3 class="h">ABS:</h3><p class="tx">Let at forme og meget holdbart, velegnet til kabinetter og automobilindustrien.</p>
    </div>
    <div class="block" style="top:132px;left:90px;width:76px">
      <h3 class="h">PS (Polystyren):</h3><p class="tx">Velegnet til lette og billige formede dele til emballage og displays.</p>
      <h3 class="h">PVC:</h3><p class="tx">Anvendes for sin alsidighed og modstandsdygtighed i industrielle applikationer.</p>
      <h3 class="h">PEHD (Polyethylen med høj densitet):</h3><p class="tx">Holdbart og kemisk resistent, ideel til tanke, kar og beholdere.</p>
      <h3 class="h">PP (Polypropylen):</h3><p class="tx">Kendt for sin lethed og kemikaliebestandighed.</p>
      <p class="tx">Disse materialer anvendes til at skabe alt fra enkle til komplekse former med høj nøjagtighed.</p>
    </div>
    <footer class="ft left"><span class="pn">8</span><span><svg class="ic"><use href="#i-phone"/></svg>40 12 34 56</span><span><svg class="ic"><use href="#i-globe"/></svg>www.vekpolymer.dk</span></footer>
  </article>
  <article class="page">
    <i class="tr"></i><i class="bl"></i>
    <header class="hd"><div class="brand"><b>VEK Polymer</b><span>Din partner i plastforarbejdning</span></div><span class="motto">Vi gør din vision til virkelighed</span></header>
    <h2 class="title"><strong>Polering af Plast:</strong>Forfining af Overflader til Perfektion</h2>
    <p class="lead block" style="top:45px;left:15px;right:10px">Hos VEK Polymer udgør polering af plast en væsentlig del af vores produktionsproces, hvor vi anvender flere metoder for at opnå den perfekte finish på hvert emne.</p>
    <div class="ph" style="left:15px;width:153px;top:62px;height:64px;background:radial-gradient(ellipse at 30% 80%,#4a8ac0 0 10%,transparent 25%),linear-gradient(135deg,#a9acb1,#5d6066 45%,#cfd1d3 70%,#3a3c40)" role="img" aria-label="Poleringsmaskine og polerede plastemner"></div>
    <div class="block" style="top:132px;left:15px;width:74px">
      <h3 class="h">Diamantpolering:</h3><p class="tx">Vi benytter diamantpolering til at opnå en ultraglat og højglans overflade på især klare materialer som akryl og polycarbonat.</p>
      <h3 class="h">Flammepolering:</h3><p class="tx">For plastemner, der kan tåle høje temperaturer, bruger vi flammepolering til at skabe glasklare kanter hurtigt og effektivt.</p>
      <h3 class="h">Manuel polering:</h3><p class="tx">Til komplekse former og detaljer udføres polering i hånden af erfarne medarbejdere med sans for detaljen.</p>
    </div>
    <div class="block" style="top:132px;left:94px;width:74px">
      <h3 class="h">Robotpolering:</h3><p class="tx">For større produktioner, hvor ensartethed og effektivitet er nøglen, anvender vi robotpolering, der sikrer identisk kvalitet på alle emner i serien.</p>
      <p class="tx">Gennem disse forskellige teknikker kan VEK Polymer garantere en overflade, der lever op til de højeste krav, både funktionelt og visuelt. Kontakt os for rådgivning om den rette metode.</p>
    </div>
    <footer class="ft" style="left:80px"><span><svg class="ic"><use href="#i-phone"/></svg>40 12 34 56</span><span><svg class="ic"><use href="#i-globe"/></svg>www.vekpolymer.dk</span><span class="pn">9</span></footer>
  </article>
</section>

<section class="spread" style="left:422px;top:571px;width:356px">
  <article class="page">
    <i class="tr"></i><i class="bl"></i>
    <header class="hd"><div class="brand"><b>VEK Polymer</b><span>Din partner i plastforarbejdning</span></div><span class="motto">Vi gør din vision til virkelighed</span></header>
    <h2 class="title">Laserskæring af Plast</h2>
    <p class="lead soft block" style="top:37px;left:11px;right:10px">Hos VEK Polymer tilbyder vi avanceret laserskæring af plast, der kombinerer høj præcision med fleksibilitet til at forme forskellige plastmaterialer som akryl, POM, PP og ABS.</p>
    <div class="ph" style="left:11px;width:76px;top:56px;height:59px;background:radial-gradient(ellipse at 60% 70%,#d9407a 0 15%,transparent 32%),radial-gradient(ellipse at 30% 35%,#5fb0d0 0 12%,transparent 28%),linear-gradient(135deg,#3a3c40,#1f2023)" role="img" aria-label="Laserskårne farvede akryldele"></div>
    <div class="ph" style="left:91px;width:73px;top:56px;height:59px;background:linear-gradient(135deg,#eef2f4,#b9c4ca 50%,#7d878d)" role="img" aria-label="Klare laserskårne plastdele"></div>
    <div class="block" style="top:122px;left:11px;width:74px">
      <h3 class="h">Teknisk Ekspertise:</h3><p class="tx">Vores laserskæringsproces sikrer rene snit og fine detaljer, selv i komplekse geometrier og tynde materialer.</p>
      <p class="tx" style="color:var(--red);font-weight:700;margin-top:2px">Fordele ved Laserskæring:</p>
      <h3 class="h">Høj Præcision:</h3><p class="tx">Laserskæring giver mulighed for ekstremt nøjagtige snit og små tolerancer.</p>
      <h3 class="h">Rene Snit:</h3><p class="tx">Processen producerer rene, polerede kanter uden behov for efterbehandling.</p>
    </div>
    <div class="block" style="top:122px;left:91px;width:74px">
      <h3 class="h">Hurtig Produktion:</h3><p class="tx">Laserskæring er hurtigere end mange traditionelle metoder, hvilket forkorter leveringstiden.</p>
      <h3 class="h">Fleksibilitet og Tilpasning:</h3><p class="tx">Vores teknologi giver mulighed for at håndtere både små serier og store produktioner med samme høje kvalitet.</p>
      <p class="tx">For yderligere information om vores laserskæring er du velkommen til at kontakte os. Vi ser frem til at hjælpe dig.</p>
    </div>
    <footer class="ft left"><span class="pn">10</span><span><svg class="ic"><use href="#i-phone"/></svg>40 12 34 56</span><span><svg class="ic"><use href="#i-globe"/></svg>www.vekpolymer.dk</span></footer>
  </article>
  <article class="page">
    <i class="tr"></i><i class="bl"></i>
    <header class="hd"><div class="brand"><b>VEK Polymer</b><span>Din partner i plastforarbejdning</span></div><span class="motto">Vi gør din vision til virkelighed</span></header>
    <h2 class="title">Bæredygtighed og Stabilitet<br>hos VEK Polymer</h2>
    <p class="lead soft block" style="top:46px;left:15px;right:10px">Hos VEK Polymer prioriterer vi bæredygtighed og stabilitet som en del af vores kerneværdier. Vi er dedikerede til miljøvenlige processer og certificeret kvalitetsstyring, der sikrer ensartede resultater i alle leverancer. Vores certificering efter internationale standarder betyder, at vi løbende dokumenterer og forbedrer vores arbejdsgange, reducerer spild og genanvender restmaterialer. Det giver vores kunder tryghed for, at hvert projekt udføres ansvarligt og med fokus på fremtiden.</p>
    <div class="block" style="top:82px;left:15px;width:74px">
      <h3 class="h">Arbejdsmiljø hos VEK Polymer</h3>
      <p class="tx">Vi sætter vores medarbejderes sikkerhed og trivsel højt og arbejder løbende på at forbedre arbejdsmiljøet i alle afdelinger. Moderne udsugning, ergonomiske arbejdspladser og løbende uddannelse er en naturlig del af hverdagen.</p>
      <h3 class="h">Kreditværdighed: Symbol på Finansiel Styrke og Stabilitet</h3>
      <p class="tx">Vi har opnået den højeste kreditvurdering, hvilket afspejler vores sunde økonomi og stabilitet som samarbejdspartner. For vores kunder betyder det tryghed og langsigtede relationer, hvor leverancer og aftaler altid overholdes.</p>
      <p class="tx">Vores certificering og stærke økonomi gør os til en pålidelig leverandør af plastløsninger til alle brancher.</p>
    </div>
    <div class="seal" style="left:104px;top:84px;width:54px;height:24px;background:linear-gradient(180deg,#2a9d6a 0 30%,#f4f6f8 30%)" role="img" aria-label="Certificeringsmærke"></div>
    <div class="seal" style="left:116px;top:130px;width:30px;height:26px;background:#e8262e" role="img" aria-label="Kreditvurderingsmærke"></div>
    <div class="seal" style="left:104px;top:174px;width:54px;height:24px;background:#f3f3f3;border:.4px solid #ccc" role="img" aria-label="Kvalitetscertifikat"></div>
    <footer class="ft" style="left:80px"><span><svg class="ic"><use href="#i-phone"/></svg>40 12 34 56</span><span><svg class="ic"><use href="#i-globe"/></svg>www.vekpolymer.dk</span><span class="pn">11</span></footer>
  </article>
</section>

<section class="spread" style="left:791px;top:571px">
  <article class="page">
    <i class="tr"></i><i class="bl"></i>
    <header class="hd"><div class="brand"><b>VEK Polymer</b><span>Din partner i plastforarbejdning</span></div><span class="motto">Vi gør din vision til virkelighed</span></header>
    <h2 class="title">Plastløsninger til Fødevareindustrien</h2>
    <p class="lead block" style="top:37px;left:10px;right:10px">Hos VEK Polymer er vi eksperter i fremstilling af plastkomponenter og maskinafskærmninger til fødevareindustrien. Vi anvender godkendte materialer som PEHD, PA, POM, PTFE og PEEK.</p>
    <div class="block" style="top:52px;left:10px;width:152px">
      <h3 class="h">Maskinafskærmninger i PC og PETG:</h3>
      <p class="tx">Vi fremstiller maskinafskærmninger i PC og PETG, der bygger hygiejne og sikkerhed ind i produktionen. Materialerne er slagfaste, lette at rengøre og giver fuldt udsyn til processen, så operatøren altid har overblik over maskinen.</p>
      <h3 class="h">Fødevaregodkendte Materialer:</h3>
      <p class="tx">Vores portefølje af fødevaregodkendte plastmaterialer omfatter:</p>
      <table class="tbl" style="margin-top:2px">
        <tr><th>Materiale</th><th>Egenskaber og anvendelse</th></tr>
        <tr><td>PEHD</td><td>Perfekt til skæreplader og glidelister, slidstærk og let at rengøre</td></tr>
        <tr><td>POM</td><td>Kendt for høj præcision og lav friktion i tandhjul og lejer</td></tr>
        <tr><td>PA</td><td>Sej og slidstærk, ideel til bevægelige komponenter</td></tr>
        <tr><td>PVDF</td><td>Fødevaregodkendt med fremragende kemikaliebestandighed</td></tr>
        <tr><td>PEEK</td><td>Tåler ekstrem varme og damp ved sterilisering</td></tr>
        <tr><td>PTFE</td><td>Slip-let overflade, kemisk inaktiv og temperaturbestandig</td></tr>
        <tr><td>PET-P</td><td>Gode glideegenskaber og høj formstabilitet</td></tr>
        <tr><td>PETG</td><td>Klar og slagfast, velegnet til afskærmninger og beholdere</td></tr>
      </table>
      <p class="tx" style="margin-top:3px">Alle materialer overholder gældende krav til fødevarekontakt og leveres med dokumentation. Kontakt os for rådgivning om valg af materiale til dit projekt.</p>
    </div>
    <div class="badge" style="left:12px;top:189px;width:14px;height:14px;background:#dde6ef;border:.4px solid #2d5a8c" role="img" aria-label="Godkendelsesmærke"></div>
    <div class="badge" style="left:34px;top:189px;width:22px;height:14px;border-radius:2px;background:#e4e4e4" role="img" aria-label="Godkendelsesmærke"></div>
    <div class="badge" style="left:64px;top:189px;width:22px;height:14px;border-radius:2px;background:#eef0f4" role="img" aria-label="Godkendelsesmærke"></div>
    <div class="badge" style="left:94px;top:187px;width:14px;height:16px;border-radius:2px;background:#2d4a8c" role="img" aria-label="Godkendelsesmærke"></div>
    <div class="badge" style="left:116px;top:189px;width:14px;height:14px;background:#5fb54a" role="img" aria-label="Godkendelsesmærke"></div>
    <footer class="ft left"><span class="pn">12</span><span><svg class="ic"><use href="#i-phone"/></svg>40 12 34 56</span><span><svg class="ic"><use href="#i-globe"/></svg>www.vekpolymer.dk</span></footer>
  </article>
  <article class="page">
    <i class="tr"></i><i class="bl"></i>
    <header class="hd"><div class="brand"><b>VEK Polymer</b><span>Din partner i plastforarbejdning</span></div><span class="motto">Vi gør din vision til virkelighed</span></header>
    <h2 class="title">Maskinafskærmning og Innovativt<br>Maskindesign hos VEK Polymer</h2>
    <p class="lead block" style="top:45px;left:14px;right:10px">Hos VEK Polymer er vi stolte af vores ekspertise i avanceret maskinafskærmning ved brug af transparente materialer som PMMA, PC og PETG, der sikrer optimal beskyttelse og overblik.</p>
    <div class="block" style="top:60px;left:14px;width:74px">
      <h3 class="h">Innovative Løsninger for Sikkerhed og Overvågning:</h3><p class="tx">Vores produkter inkluderer afskærmninger, døre og låg, der giver operatører fuldt udsyn til processen og samtidig beskytter mod ulykker og støj.</p>
      <h3 class="h">Fødevaresikkerhed:</h3><p class="tx">For industrier med specifikke krav til hygiejne tilbyder vi løsninger i godkendte materialer, der tåler hyppig rengøring.</p>
      <h3 class="h">Teknologisk Avancerede Fremstillingsteknikker:</h3><p class="tx">Vi tilbyder en række designløsninger gennem specialiseret fræsning, bukning og limning, som sikrer præcise og holdbare afskærmninger.</p>
    </div>
    <div class="block" style="top:60px;left:94px;width:72px">
      <h3 class="h">Fleksibilitet og Skalerbarhed:</h3><p class="tx">Vores kapacitet i materialehåndtering og designfleksibilitet er uovertruffen. Vi leverer alt fra enkeltstykker til store serier med samme høje kvalitet, og vi tilpasser hver løsning til maskinens funktion.</p>
      <p class="tx">For mere information om, hvordan vi kan hjælpe med jeres næste projekt, er I velkomne til at kontakte os.</p>
    </div>
    <div class="ph" style="left:14px;width:74px;top:178px;height:44px;background:linear-gradient(135deg,#5a5c60,#1e1f22 50%,#b9bdc0)" role="img" aria-label="Transparent maskinafskærmning"></div>
    <div class="ph" style="left:92px;width:74px;top:178px;height:44px;background:linear-gradient(135deg,#2a2b2e,#c9b58a 45%,#8a7a5a 75%,#3a3b3e)" role="img" aria-label="Klar bukket plastskærm"></div>
    <footer class="ft" style="left:80px"><span><svg class="ic"><use href="#i-phone"/></svg>40 12 34 56</span><span><svg class="ic"><use href="#i-globe"/></svg>www.vekpolymer.dk</span><span class="pn">13</span></footer>
  </article>
</section>

<!-- Row 4 -->
<section class="spread" style="left:48px;top:836px;width:360px;height:255px">
  <article class="page">
    <i class="tr"></i><i class="bl"></i>
    <header class="hd"><div class="brand"><b>VEK Polymer</b><span>Din partner i plastforarbejdning</span></div><span class="motto">Vi gør din vision til virkelighed</span></header>
    <h2 class="title">Tilpassede Nyseskærme og<br>Udstillingsmontrer fra VEK Polymer</h2>
    <div class="block" style="top:53px;left:10px;width:74px">
      <h3 class="h" style="font-weight:600">Skræddersyede Nyseskærme for Alle Brancher</h3>
      <p class="lead">VEK Polymer specialiserer sig i produktionen af tilpassede nyseskærme, der opfylder behov i mange brancher. Vi tilbyder løsninger, der matcher indretning og funktion.</p>
      <h3 class="h">Detailbutikker og Supermarkeder:</h3><p class="tx">Vores nyseskærme beskytter både kunder og personale og passer til alle typer diske og kasseområder.</p>
      <h3 class="h">Apoteker:</h3><p class="tx">Med hygiejne i fokus leverer vi specialdesignede løsninger til apoteker og klinikker.</p>
      <h3 class="h">Restauranter og Caféer:</h3><p class="tx">Diskrete skærme, der bevarer en indbydende atmosfære for gæsterne.</p>
      <h3 class="h">Bageriforretninger:</h3><p class="tx">Vi producerer skærme, der beskytter varerne og samtidig viser dem frem bedst muligt.</p>
      <p class="tx">Vores ekspertise sikrer holdbare og praktiske løsninger.</p>
    </div>
    <div class="block" style="top:53px;left:90px;width:76px">
      <h3 class="h" style="font-weight:600">Udstillingsmontrer til Danske Museer</h3>
      <p class="lead">VEK Polymer tilbyder avancerede løsninger i design og fremstilling af udstillingsmontrer til museer og gallerier.</p>
      <h3 class="h">Design og Tilpasning:</h3><p class="tx">Vi arbejder tæt sammen med museer for at skabe montrer, der fremhæver genstandene optimalt og beskytter dem mod støv og berøring.</p>
      <h3 class="h">Materialer og Fremstilling:</h3><p class="tx">Vores montrer fremstilles af højkvalitets akryl, der sikrer klarhed og holdbarhed. Alle samlinger UV-limes for et usynligt resultat.</p>
      <p class="tx">For yderligere information om, hvordan vi kan hjælpe, er du velkommen til at kontakte os.</p>
    </div>
    <footer class="ft left"><span class="pn">14</span><span><svg class="ic"><use href="#i-phone"/></svg>40 12 34 56</span><span><svg class="ic"><use href="#i-globe"/></svg>www.vekpolymer.dk</span></footer>
  </article>
  <article class="page">
    <i class="tr"></i><i class="bl"></i>
    <header class="hd"><div class="brand"><b>VEK Polymer</b><span>Din partner i plastforarbejdning</span></div><span class="motto">Vi gør din vision til virkelighed</span></header>
    <h2 class="title">Oversigt over Tekniske<br>Plastmaterialer hos VEK Polymer</h2>
    <div class="ph" style="left:15px;width:152px;top:56px;height:66px;background:linear-gradient(135deg,#e9e6df,#5aa05a 25%,#1f2023 45%,#e07a2a 65%,#f2f2f2 80%,#3a3b3e)" role="img" aria-label="Stakke af farvede plastplader og stænger"></div>
    <div class="block" style="top:132px;left:15px;width:152px">
      <table class="tbl">
        <tr><th>Polymer</th><th>Betegnelse</th><th>Egenskaber</th><th>Anvendelse</th></tr>
        <tr><td>Polyetheretherketon</td><td>PEEK</td><td>Fremragende varmebestandighed og styrke</td><td>Spåntagning</td></tr>
        <tr><td>Polyethylentereftalat</td><td>PET-P</td><td>Præcis, formstabil og slidstærk</td><td>Spåntagning</td></tr>
        <tr><td>Polytetrafluorethylen</td><td>PTFE</td><td>Lav friktion, kemisk inaktiv</td><td>Spåntagning</td></tr>
        <tr><td>Polyvinyliden fluorid</td><td>PVDF</td><td>Høj kemisk resistens og renhed</td><td>Spåntagning</td></tr>
        <tr><td>Polyamide (Nylon)</td><td>PA6, PA66</td><td>God slidstyrke og sejhed</td><td>Spåntagning</td></tr>
        <tr><td>Polyoxymethylene</td><td>POM</td><td>Lav friktion, høj stivhed</td><td>Spåntagning</td></tr>
        <tr><td>Polyethylene</td><td>PEHD 300</td><td>Moderat slidstyrke, let at svejse</td><td>Svejsning, bukning</td></tr>
        <tr><td>Polyethylene</td><td>PEHD 500</td><td>Forbedret slidstyrke og sejhed</td><td>Spåntagning</td></tr>
        <tr><td>Polyethylene</td><td>PEHD 1000</td><td>Maksimal slidstyrke og slagfasthed</td><td>Spåntagning</td></tr>
      </table>
    </div>
    <footer class="ft" style="left:80px"><span><svg class="ic"><use href="#i-phone"/></svg>40 12 34 56</span><span><svg class="ic"><use href="#i-globe"/></svg>www.vekpolymer.dk</span><span class="pn">15</span></footer>
  </article>
</section>

<section class="spread" style="left:422px;top:836px;width:356px;height:255px">
  <article class="page">
    <i class="tr"></i><i class="bl"></i>
    <header class="hd"><div class="brand"><b>VEK Polymer</b><span>Din partner i plastforarbejdning</span></div><span class="motto">Vi gør din vision til virkelighed</span></header>
    <div class="block" style="top:28px;left:10px;right:10px">
      <table class="tbl">
        <tr><th>Polymer</th><th>Betegnelse</th><th>Egenskaber</th><th>Anvendelse</th></tr>
        <tr><td>Acrylonitril Styren Acrylat</td><td>ASA</td><td>UV- og slagbestandig, god farvestabilitet</td><td>Limning, bukning, vakuumformning</td></tr>
        <tr><td>Acrylonitril Butadien Styren</td><td>ABS</td><td>Høj slagstyrke, let at forme</td><td>Limning, bukning, vakuumformning</td></tr>
        <tr><td>Polystyren</td><td>PS</td><td>Let og økonomisk materiale</td><td>Limning, bukning</td></tr>
        <tr><td>Polypropylen</td><td>PP</td><td>Kemisk resistent og let</td><td>Svejsning, bukning</td></tr>
        <tr><td>Polyvinylchlorid</td><td>PVC</td><td>Robust, holdbar og brandhæmmende</td><td>Spåntagning, limning, bukning</td></tr>
        <tr><td>Polyethylentereftalat glykol</td><td>PETG</td><td>Klar, slagfast og fødevaregodkendt</td><td>Spåntagning, formning</td></tr>
        <tr><td>Polymethyl Methacrylate</td><td>PMMA</td><td>Høj gennemsigtighed og glans</td><td>Laserskæring, limning, bukning</td></tr>
        <tr><td>Polycarbonat</td><td>PC</td><td>Høj slagfasthed og klarhed</td><td>Spåntagning, formning</td></tr>
      </table>
    </div>
    <svg class="block" style="top:138px;left:28px" width="120" height="100" viewBox="0 0 120 100" role="img" aria-label="Pyramide over plastmaterialer inddelt efter temperatur og ydeevne">
      <defs><linearGradient id="pyr" x1="0" y1="0" x2="0" y2="1"><stop offset="0" stop-color="#f5a623"/><stop offset=".45" stop-color="#d2232a"/><stop offset=".8" stop-color="#7a1f5c"/><stop offset="1" stop-color="#3a3a8c"/></linearGradient></defs>
      <polygon points="60,2 112,96 8,96" fill="url(#pyr)"/>
      <g stroke="#fff" stroke-width=".4"><line x1="60" y1="2" x2="60" y2="96"/><line x1="40" y1="38" x2="80" y2="38"/><line x1="27" y1="62" x2="93" y2="62"/><line x1="18" y1="80" x2="102" y2="80"/></g>
      <g font-family="Montserrat,sans-serif" font-size="2.6" fill="#333"><text x="82" y="36">150 °C</text><text x="95" y="60">100 °C</text><text x="2" y="30">Højtydende plast</text><text x="0" y="58">Tekniske plast</text><text x="0" y="92">Standardplast</text></g>
      <g font-family="Montserrat,sans-serif" font-size="2.2" fill="#fff"><text x="54" y="26">PEEK</text><text x="62" y="50">POM</text><text x="46" y="50">PA</text><text x="62" y="73">PETG</text><text x="46" y="73">PC</text><text x="48" y="90">PE, PP, PS</text></g>
    </svg>
    <footer class="ft left"><span class="pn">16</span><span><svg class="ic"><use href="#i-phone"/></svg>40 12 34 56</span><span><svg class="ic"><use href="#i-globe"/></svg>www.vekpolymer.dk</span></footer>
  </article>
  <article class="page">
    <i class="tr"></i><i class="bl"></i>
    <header class="hd"><div class="brand"><b>VEK Polymer</b><span>Din partner i plastforarbejdning</span></div><span class="motto">Vi gør din vision til virkelighed</span></header>
    <h2 class="title">VEK Polymer:<br>Din Partner i Skræddersyede<br>Plastløsninger</h2>
    <div class="ph" style="left:27px;width:98px;top:58px;height:82px;background:radial-gradient(ellipse at 50% 50%,#3a3a3c 0 30%,#1b1b1d 45%,rgba(255,255,255,0) 62%)" role="img" aria-label="Bunke af sorte sprøjtestøbte plastdele"></div>
    <div class="block" style="top:146px;left:10px;width:76px">
      <h3 class="h">Skræddersyede Plastløsninger hos VEK Polymer</h3>
      <p class="tx">Med vores omfattende teknologi og mere end 35 års erfaring leverer vi løsninger til industrier, der kræver præcision og pålidelighed. Vores maskinpark spænder over CNC-fræsning, drejning, laserskæring og vakuumformning.</p>
      <h3 class="h">Totalløsninger og Overstigelse af Forventninger</h3>
      <p class="tx">Vores mål er at overgå kundernes forventninger ved at tilbyde totalløsninger fra idé til færdigt produkt, med rådgivning undervejs og levering til tiden.</p>
    </div>
    <div class="block" style="top:146px;left:90px;width:76px">
      <h3 class="h">Certificeringer og Kvalitetsgaranti</h3>
      <p class="tx">Vi er stolte af vores certificeringer og den høje kreditvurdering, som afspejler vores stabilitet og kvalitet. Det giver dig som kunde tryghed i samarbejdet.</p>
      <h3 class="h">Åbenhed og Samarbejde</h3>
      <p class="tx">Alle oplysninger i denne brochure er ment som inspiration. Kontakt os for at drøfte netop dit projekt, så finder vi sammen den rette løsning. Vi ser frem til at høre fra dig.</p>
    </div>
    <footer class="ft" style="left:80px"><span><svg class="ic"><use href="#i-phone"/></svg>40 12 34 56</span><span><svg class="ic"><use href="#i-globe"/></svg>www.vekpolymer.dk</span><span class="pn">17</span></footer>
  </article>
</section>

<section class="spread" style="left:791px;top:836px;height:255px">
  <article class="page">
    <i class="tr"></i><i class="bl"></i>
    <header class="hd"><div class="brand"><b>VEK Polymer</b><span>Din partner i plastforarbejdning</span></div><span class="motto">Vi gør din vision til virkelighed</span></header>
    <div class="help-band">
      <h2>Vi står klar til at hjælpe dig</h2>
      <p>Tak for din interesse i VEK Polymer. Vi er dedikerede til at levere fremragende plastløsninger og står klar til at assistere dig med din næste udfordring. Besøg vores produktionsanlæg i Hørning og se vores maskinpark i drift – vi viser gerne rundt og fortæller om vores arbejde.</p>
      <p>Vi opfordrer dig til at kontakte os eller personligt besøge vores facilitet, hvor du kan udforske de mange muligheder inden for plastbearbejdning. Vores løsninger er skræddersyede til dit behov.</p>
      <p>For mere information eller for at planlægge et besøg, kontakt os venligst. Vi ser frem til et samarbejde præget af præcision, innovation og håndværksmæssig ekspertise.</p>
    </div>
    <footer class="ft left"><span class="pn">18</span><span><svg class="ic"><use href="#i-phone"/></svg>40 12 34 56</span><span><svg class="ic"><use href="#i-globe"/></svg>www.vekpolymer.dk</span></footer>
  </article>
  <article class="page">
    <i class="tr"></i><i class="bl"></i>
    <header class="hd"><div class="brand"><b>VEK Polymer</b><span>Din partner i plastforarbejdning</span></div><span class="motto">Vi gør din vision til virkelighed</span></header>
    <div class="ph" style="left:14px;width:152px;top:59px;height:177px;background:radial-gradient(ellipse at 55% 75%,#2a5fb8 0 10%,transparent 24%),radial-gradient(ellipse at 70% 40%,#b88a3a 0 6%,transparent 16%),linear-gradient(170deg,#3a3c40,#e6e8ea 35%,#a9b0b5 60%,#4a5055)" role="img" aria-label="Diplomer og blå plastkomponenter i udstillingsmontre"></div>
    <footer class="ft" style="left:80px"><span><svg class="ic"><use href="#i-phone"/></svg>40 12 34 56</span><span><svg class="ic"><use href="#i-globe"/></svg>www.vekpolymer.dk</span><span class="pn">19</span></footer>
  </article>
</section>
</body>
</html>
```